Holiday Rental Company Flyer Design (DL not A5)

Note from PixelFolk Administration: The category sizing selected is A5, however the project requires DL sized artwork. Please refer to the DL template link below while the 'Special Requirements' are updated accordingly.

Project Brief:
We need a double sided DL flyer designed for an up market Holiday Rental Company that portrays a personalised approach to property management. These are to be used for letter box drops to homes we're specifically targeting so the design should be modern, complimentary colour palette, uncluttered & visually appealing.

Please Download the DL Template from Quillmark here: http://www.quillmark.com.au/qm/ns/propath/UploadResources.aspx?selectedTab=0?pfid=BFB&pf_id=BFB&xnav=easypath-upload-image#Templates

Target Market(s)

Wealthy Home Owners

Industry/Entity Type

It Company

Font styles to use
Other font styles liked:
• Avant Garde Extra Light & Demi

Colors
33b8a4

Requirements
Must have
• DL Flyer sizes (210mm width x 99mm width, plus 3mm bleed)
• Front: Logo, Main Image & Grab
• Back: Contact Details & Brief Description of our business
• Images: Ideally the main image should be the house with the pool but alternatively a lifestyle images could also be used.
Nice to have
• A creative designer!
Should not have
• Clutter & busy designs

```html
<!DOCTYPE html>
<html lang="en">
<head>
<meta charset="utf-8">
<title>Harbourline Stays – DL Flyer</title>
<link rel="stylesheet" href="https://fonts.googleapis.com/css2?family=Lato:wght@300;700&family=Oswald:wght@400;700&display=swap">
<style>
  :root {
    --teal: #1aaa93;
    --teal-dark: #12907c;
    --teal-deep: #0c6f60;
    --ink: #3d3d3d;
    --grey-text: #5a5a5a;
    --paper: #f6f6f6;
    --page-bg: #2b2b2b;
    --white: #ffffff;
    --night-1: #1d1f5c;
    --night-2: #5e4fa6;
    --warm: #c9a35a;
    --pool: #3a8fe0;
  }
  * { margin: 0; padding: 0; box-sizing: border-box; }
  html, body {
    width: 668px; height: 1200px; overflow: hidden;
    background: var(--page-bg);
    font-family: "Lato", Arial, sans-serif;
  }
  .flyer {
    position: absolute; left: 84px; top: 90px;
    width: 502px; height: 1020px;
    background: linear-gradient(180deg, var(--white) 0%, var(--paper) 60%, #ececec 100%);
    overflow: hidden;
  }
  .hero-photo {
    position: absolute; left: 0; top: 0; width: 502px; height: 380px;
    background:
      linear-gradient(90deg, rgba(201,163,90,.85) 0%, rgba(120,100,80,.6) 30%, rgba(0,0,0,0) 55%),
      linear-gradient(180deg, var(--night-1) 0%, var(--night-2) 55%, #8f87c9 75%, var(--pool) 90%, #2f76c8 100%);
  }
  .layer { position: absolute; left: 0; top: 0; }
  .brand-pennant {
    position: absolute; left: 26px; top: 288px; width: 190px; height: 224px;
  }
  .brand-name {
    position: absolute; left: 26px; top: 362px; width: 190px;
    text-align: center; color: var(--white);
    font-weight: 300; font-size: 24px; letter-spacing: 2px; line-height: 1.15;
  }
  .headline {
    position: absolute; right: 42px; top: 412px; text-align: right;
  }
  .headline-main {
    font-family: "Oswald", Impact, sans-serif; font-weight: 700;
    font-size: 52px; line-height: 1; color: var(--teal); letter-spacing: 1px;
  }
  .headline-sub {
    font-family: "Oswald", Arial, sans-serif; font-weight: 400;
    font-size: 22px; color: var(--ink); margin-top: 4px; letter-spacing: .5px;
  }
  .headline-copy {
    position: absolute; right: 42px; top: 504px; width: 330px;
    text-align: right; color: var(--teal);
    font-weight: 700; font-size: 16.5px; line-height: 1.26;
  }
  .feature {
    position: absolute; top: 612px; width: 128px; height: 128px;
    border-radius: 50%; background: var(--teal);
    display: flex; align-items: center; justify-content: center;
    box-shadow: 0 2px 4px rgba(0,0,0,.15);
  }
  .feature-photo {
    width: 92px; height: 92px; border-radius: 50%;
    border: 5px solid var(--white);
  }
  .feature--bath { left: 30px; }
  .feature--bath .feature-photo { background: radial-gradient(circle at 40% 40%, #e8e6e2, #a9a6a0); }
  .feature--flowers { left: 180px; }
  .feature--flowers .feature-photo { background: radial-gradient(circle at 50% 40%, #d7833e, #6b5a48 70%); }
  .feature--cushions { left: 330px; }
  .feature--cushions .feature-photo { background: radial-gradient(circle at 50% 50%, #e5d64a, #b59a5c 70%); }
  .enquiry-copy {
    position: absolute; left: 20px; top: 764px; width: 462px;
    text-align: center; color: var(--grey-text);
    font-weight: 700; font-size: 16.5px; line-height: 1.3;
  }
  .contact {
    position: absolute; left: 0; top: 890px; width: 502px;
    color: var(--white); font-size: 22px; line-height: 30px; text-align: center;
  }
  .contact-line { display: flex; align-items: center; justify-content: center; gap: 8px; }
  .contact-icon { width: 22px; height: 22px; flex: none; }
</style>
</head>
<body>
<main class="flyer">
  <div class="hero-photo" role="img" aria-label="Modern luxury home at dusk with lit interiors and a blue swimming pool with water feature"></div>

  <svg class="layer" width="502" height="1020" viewBox="0 0 502 1020" aria-hidden="true">
    <!-- top sweep -->
    <path d="M0 320 C160 300 330 330 502 372 L502 1020 L0 1020 Z" fill="var(--teal)"/>
    <path d="M0 338 C170 320 340 350 502 392 L502 1020 L0 1020 Z" fill="var(--white)"/>
    <path d="M0 346 C170 330 340 360 502 402 L502 1020 L0 1020 Z" fill="#f8f8f8"/>
    <!-- faint wave behind features -->
    <path d="M0 640 C140 590 300 600 502 650 L502 700 C300 660 150 660 0 700 Z" fill="#e4e4e4" opacity=".6"/>
    <!-- bottom band -->
    <path d="M0 862 C180 850 330 850 502 862 L502 1020 L0 1020 Z" fill="var(--teal)"/>
    <path d="M0 862 C180 846 330 846 502 862 L502 868 C330 854 180 854 0 868 Z" fill="var(--white)"/>
  </svg>

  <svg class="brand-pennant" viewBox="0 0 190 224" aria-hidden="true">
    <path d="M10 0 L180 0 L190 14 L0 14 Z" fill="#111"/>
    <path d="M0 14 L190 14 L190 160 L95 224 L0 160 Z" fill="var(--teal)"/>
  </svg>
  <div class="brand-name">HARBOURLINE<br>STAYS</div>

  <div class="headline">
    <div class="headline-main">WHAT WE</div>
    <div class="headline-sub">DO DIFFERENTLY!</div>
  </div>
  <p class="headline-copy">Rather than relying upon a key safe or a central pick-up destination, a ‘Harbourline Stays’ staff member will greet guests upon arrival.</p>

  <div class="feature feature--bath"><div class="feature-photo" role="img" aria-label="Bathroom basin and tap detail"></div></div>
  <div class="feature feature--flowers"><div class="feature-photo" role="img" aria-label="Vase of orange flowers on a table"></div></div>
  <div class="feature feature--cushions"><div class="feature-photo" role="img" aria-label="Yellow cushions on a sofa"></div></div>

  <p class="enquiry-copy">If you’d like to know what your property could achieve or require additional information, please contact us on:</p>

  <div class="contact">
    <div class="contact-line">
      <svg class="contact-icon" viewBox="0 0 22 22"><rect x="1" y="1" width="20" height="20" rx="3" fill="var(--white)"/><path d="M7 5 C5 6 5 9 7 12 C9 15 12 17 14 17 L16 15 L13.5 12.5 L12 13.5 C10.5 12.5 9.5 11 9 9.5 L10 8 L8 5 Z" fill="var(--teal)"/></svg>
      <span>(03)5550 0142</span>
    </div>
    <div class="contact-line">
      <svg class="contact-icon" viewBox="0 0 22 22"><rect x="1" y="5" width="20" height="13" fill="var(--white)"/><path d="M1 5 L11 13 L21 5" fill="none" stroke="var(--teal)" stroke-width="1.5"/></svg>
      <span>stay@harbourlinestays.com.au</span>
    </div>
    <div class="contact-line">
      <svg class="contact-icon" viewBox="0 0 22 22" fill="none" stroke="var(--white)" stroke-width="1.6"><circle cx="11" cy="11" r="9"/><ellipse cx="11" cy="11" rx="4" ry="9"/><path d="M2 11 H20 M4 6 H18 M4 16 H18"/></svg>
      <span>harbourlinestays.com.au</span>
    </div>
  </div>
</main>
</body>
</html>
```